WP website design (Durham)

We need a wordpress design that will incorporate a professional color scheme with company logo in a clean layout. The design needs to consider that this will be developed on a responsive theme. Colors are undetermined - subdued or subtle, perhaps earth tones colors will likely work well. Logo color can be changed from black to any other to suit.

Client wants a unique look for their site - mentions liking http://www.rvtolan.com/ and http://www.brimscottauction.com/. Possible but not necessary to have large slideshow element.

Industry/Entity Type

It Company

Font styles to use
Serif
Sans Serif

Colors

Designer to choose colors to be used in the design.

Requirements
Must have
• Navigation: 1)Home 2) Auctions 3) For Sale 4) Buyers & Sellers 5) Brokerage 6) About Us 7) Contact Us

Site will have slideshow, please use high-end stock real estate image initially. Header will have logo. Social icons (Facebook, Twitter, Youtube) and tagline "THE REAL ESTATE AUCTION AUTHORITY SINCE 1977" will be used.

Widgets Include: Email signup form, Featured Auctions, News & Events Blog, Featured Video widget.

Footer will have contact info (below), site navigation, smaller company logo, testimonial widget, affiliation logos (attached).
Nice to have
• Site will have drop-down menus - please indicate the styling, for instance the dropdown menus 1) Referrals 2) Properties For Sale under the 'Brokerage' link

```html
<!DOCTYPE html>
<html lang="en">
<head>
<meta charset="utf-8">
<title>J. Harlow &amp; Associates</title>
<link rel="stylesheet" href="https://fonts.googleapis.com/css2?family=Arvo:wght@400;700&family=Montserrat:wght@400;500&family=Open+Sans:wght@400;600&display=swap">
<style>
:root{
  --page:#ffffff;
  --column:#e4e4e4;
  --navy:#2b3042;
  --charcoal:#252525;
  --footer:#3c3c3c;
  --orange:#c6782b;
  --text:#444;
  --line:#cfcfcf;
}
*{box-sizing:border-box;margin:0;padding:0}
html,body{width:1020px;height:1200px;overflow:hidden;background:var(--page)}
body{position:relative;font-family:'Open Sans',sans-serif;color:var(--text)}
.abs{position:absolute}
.column{left:106px;top:0;width:806px;height:1026px;background:var(--column)}
.brand{left:121px;top:24px;font-family:'Montserrat',sans-serif;font-weight:400;font-size:25px;color:#222;letter-spacing:-.5px}
.connect{left:687px;top:36px;display:flex;align-items:center;gap:6px;font-family:'Montserrat',sans-serif;font-size:15px;color:#222}
.connect span{margin-right:6px;letter-spacing:.5px}
.social{display:flex;align-items:center;justify-content:center;width:18px;height:18px;background:#111;border-radius:3px}
.social::after{content:"";width:6px;height:6px;border-radius:50%;background:#fff}
.nav{left:97px;top:87px;width:824px;height:33px;background:var(--charcoal);border-radius:8px 8px 3px 3px;display:flex;align-items:center;padding-left:16px;gap:25px;font-family:'Montserrat',sans-serif;font-size:13px;color:#fff}
.nav .active{color:var(--orange)}
.hero{left:107px;top:129px;width:806px;height:287px;background:var(--navy);border-radius:3px}
.hero-photo{left:118px;top:141px;width:784px;height:264px;background:linear-gradient(180deg,#b9c8d8 0%,#dfe4e6 35%,#eae8e2 60%,#7f8f6a 85%,#6a7459 100%)}
.hero-card{left:129px;top:239px;width:276px;height:154px;background:rgba(30,30,30,.72);padding:11px 20px 0 22px;color:#fff}
.hero-card h1{font-family:'Arvo',serif;font-weight:700;font-size:15px;line-height:19px;text-align:center;white-space:nowrap;letter-spacing:0;margin-left:-8px;margin-right:-8px}
.hero-card p{font-family:'Montserrat',sans-serif;font-size:9.5px;line-height:15px;margin-top:14px}
.hero-card .field{margin-top:6px;height:25px;background:#d4d4d4;border:1px solid #aaa;font-style:italic;font-size:11px;color:#555;padding:5px 11px;width:231px}
.hero-card .btn{display:inline-block;margin-top:9px;background:var(--orange);font-family:'Montserrat',sans-serif;font-size:10.5px;padding:3px 11px}
.dropdown{left:459px;top:129px;width:95px;height:59px;background:rgba(90,90,90,.85);padding:6px 6px;display:flex;flex-direction:column;gap:3px}
.dropdown::before{content:"";position:absolute;left:17px;top:-7px;border:7px solid transparent;border-top:0;border-bottom-color:#bbb}
.dropdown span{font-family:'Montserrat',sans-serif;font-size:7px;color:#fff;background:#3a3a3a;padding:2px 5px;height:12px}
.dropdown span.on{background:var(--orange)}
.panel{background:#fff;border:1px solid #cfcfcf;border-radius:3px}
.welcome{left:123px;top:459px;width:493px;height:555px}
.welcome h2{position:absolute;left:14px;top:18px;font-family:'Montserrat',sans-serif;font-weight:500;font-size:13.5px;color:#111}
.welcome p{position:absolute;left:14px;top:43px;width:465px;font-size:11px;line-height:19px;color:#555}
.featured-bar{left:135px;top:596px;width:457px;height:31px;background:var(--navy);color:#fff;font-family:'Arvo',serif;font-weight:700;font-size:14.5px;padding:7px 10px;letter-spacing:.3px}
.divider{left:138px;top:821px;width:455px;height:1px;background:var(--line)}
.card{width:184px;height:137px;border:3px solid #ddd;background:#fff;padding:6px}
.card .thumb{position:absolute;left:6px;top:6px;width:70px;height:68px;background:linear-gradient(180deg,#a9bdd0,#6f7b86 55%,#6d7f52);border:1px solid #999}
.card h3{position:absolute;left:84px;top:11px;font-family:'Arvo',serif;font-weight:400;font-size:8.5px;color:#222}
.card .body{position:absolute;left:84px;top:30px;width:88px;font-size:5.5px;line-height:10px;color:#777}
.card .tags{position:absolute;left:12px;top:84px;display:flex;gap:6px}
.card .tags span{font-size:3.5px;color:#fff;background:#555c66;border-radius:4px;padding:1px 4px}
.card .bid{position:absolute;left:6px;top:104px;font-size:4px;line-height:7px;color:#555}
.card .go{position:absolute;left:84px;top:100px;width:84px;height:20px;background:var(--orange);color:#fff;font-family:'Montserrat',sans-serif;font-size:7.5px;text-align:center;line-height:20px;box-shadow:1px 1px 0 #8a5320}
.side-title{font-family:'Arvo',serif;font-weight:700;font-size:17px;color:var(--navy);text-align:center}
.news{left:650px;top:459px;width:249px;height:217px}
.news .side-title{margin-top:12px}
.item{position:absolute;left:9px;width:230px}
.item .date{position:absolute;left:0;top:0;width:31px;text-align:center;font-family:'Montserrat',sans-serif;font-size:11px}
.item .date b{display:block;height:20px;line-height:20px;background:var(--orange);color:#222;font-weight:500}
.item .date em{display:block;height:15px;line-height:15px;background:var(--navy);color:#fff;font-style:normal;font-weight:500}
.item p{position:absolute;left:37px;top:-2px;width:190px;font-family:'Montserrat',sans-serif;font-size:9px;line-height:14.5px;color:#444}
.item p a{color:var(--orange);text-decoration:none}
.news .rule{position:absolute;left:10px;top:120px;width:228px;height:1px;background:var(--line)}
.video{left:650px;top:702px;width:249px;height:218px}
.video .side-title{margin-top:10px}
.player{position:absolute;left:17px;top:59px;width:208px;height:124px;border:2px solid var(--orange);background:linear-gradient(180deg,#3e4654 0%,#7a6a58 50%,#4f5e3c 100%)}
.player svg{position:absolute;left:0;top:0}
.footer{left:0;top:1026px;width:1020px;height:133px;background:var(--footer)}
.foot-brand{left:111px;top:1063px;width:162px;height:46px;background:#fff;color:#222;font-family:'Montserrat',sans-serif;font-size:13.5px;text-align:center;line-height:46px;white-space:nowrap}
.contact{left:301px;top:1055px;color:#fff;font-family:'Montserrat',sans-serif}
.contact h4{font-weight:400;font-size:15.5px}
.contact p{font-size:11px;margin-top:6px;display:flex;align-items:center;gap:8px}
.badges{left:663px;top:1073px;display:flex;gap:10px;align-items:center}
.badges i{display:block;width:33px;height:36px;background:#d8d8d8;border-radius:3px}
.bottom{left:0;top:1159px;width:1020px;height:41px;background:var(--navy);color:#fff;font-family:'Montserrat',sans-serif;font-size:9px}
.bottom nav{position:absolute;left:107px;top:15px;display:flex;gap:9px}
.bottom .copy{position:absolute;right:106px;top:15px}
</style>
</head>
<body>
<div class="abs column"></div>

<header>
  <div class="abs brand">J.Harlow &amp; Associates</div>
  <div class="abs connect"><span>Connect with Us</span><i class="social" aria-label="Social link"></i><i class="social" aria-label="Social link"></i><i class="social" aria-label="Social link"></i></div>
  <nav class="abs nav">
    <span>Home</span><span>Auctions</span><span>For Sale</span><span>Buyer and Sellers</span><span class="active">Brokerage</span><span>About Us</span><span>Contact Us</span>
  </nav>
</header>

<section>
  <div class="abs hero"></div>
  <div class="abs hero-photo" role="img" aria-label="Photo of a modern white two-storey house with grey roof under a cloudy sky"></div>
  <div class="abs hero-card">
    <h1>THE REAL ESTATE AUCTION<br>AUTHORITY SINCE 1977</h1>
    <p>Lorem ipsum is a dummy text only. Dolor sit amet, consectetur adipiscing elit.</p>
    <div class="field">Enter Email Address</div>
    <span class="btn">Sign Up Now</span>
  </div>
  <div class="abs dropdown"><span class="on">Lorem Ipsum Text</span><span>Lorem Ipsum Text</span><span>Lorem Ipsum Text</span></div>
</section>

<main>
  <div class="abs panel welcome">
    <h2>Welcome to J. Harlow</h2>
    <p>Lorem ipsum is a dummy text only. Dolor sit amet, consectetur adipiscing elit. Nullam felis mauris, eleifend ac rhoncus non, lobortis at diam. Pellentesque suscipit nulla sit amet venenatis porttitor. In augue felis, venenatis id auctor a, sagittis non ligula.</p>
  </div>
  <div class="abs featured-bar">FEATURED AUCTIONS</div>

  <div class="abs card" style="left:168px;top:654px">
    <div class="thumb" role="img" aria-label="Photo of a grey two-storey house with garage"></div>
    <h3>Pellentesque acsan</h3>
    <div class="body">Lorem ipsum is a dummy text only. Dolor sit amet, consectetur adipiscing elit. Nullam felis mauris, eleifend ac rhoncus non, lobortis at diam rume.</div>
    <div class="tags"><span>View details</span><span>View gallery</span></div>
    <div class="bid">Online bidding<br>Began: 07/24/14 at 5:00 PM CDT<br>Ends: 08/25/14 at 8:00 PM CDT</div>
    <div class="go">Click to bid online</div>
  </div>
  <div class="abs card" style="left:382px;top:654px">
    <div class="thumb" role="img" aria-label="Photo of a grey two-storey house with garage"></div>
    <h3>Pellentesque acsan</h3>
    <div class="body">Lorem ipsum is a dummy text only. Dolor sit amet, consectetur adipiscing elit. Nullam felis mauris, eleifend ac rhoncus non, lobortis at diam rume.</div>
    <div class="tags"><span>View details</span><span>View gallery</span></div>
    <div class="bid">Online bidding<br>Began: 07/24/14 at 5:00 PM CDT<br>Ends: 08/25/14 at 8:00 PM CDT</div>
    <div class="go">Click to bid online</div>
  </div>
  <div class="abs divider"></div>
  <div class="abs card" style="left:168px;top:847px">
    <div class="thumb" role="img" aria-label="Photo of a grey two-storey house with garage"></div>
    <h3>Pellentesque acsan</h3>
    <div class="body">Lorem ipsum is a dummy text only. Dolor sit amet, consectetur adipiscing elit. Nullam felis mauris, eleifend ac rhoncus non, lobortis at diam rume.</div>
    <div class="tags"><span>View details</span><span>View gallery</span></div>
    <div class="bid">Online bidding<br>Began: 07/24/14 at 5:00 PM CDT<br>Ends: 08/25/14 at 8:00 PM CDT</div>
    <div class="go">Click to bid online</div>
  </div>
  <div class="abs card" style="left:382px;top:847px">
    <div class="thumb" role="img" aria-label="Photo of a grey two-storey house with garage"></div>
    <h3>Pellentesque acsan</h3>
    <div class="body">Lorem ipsum is a dummy text only. Dolor sit amet, consectetur adipiscing elit. Nullam felis mauris, eleifend ac rhoncus non, lobortis at diam rume.</div>
    <div class="tags"><span>View details</span><span>View gallery</span></div>
    <div class="bid">Online bidding<br>Began: 07/24/14 at 5:00 PM CDT<br>Ends: 08/25/14 at 8:00 PM CDT</div>
    <div class="go">Click to bid online</div>
  </div>

  <aside>
    <div class="abs panel news">
      <div class="side-title">Latest News &amp; Events</div>
      <div class="item" style="top:60px">
        <div class="date"><b>Sep</b><em>26</em></div>
        <p>Lorem ipsum is a dummy text only.<br>Dolor sit amet, consectetur adipiscing<br>elit. Nullam felis mauris....<a>[Read more]</a></p>
      </div>
      <div class="rule"></div>
      <div class="item" style="top:139px">
        <div class="date"><b>Sep</b><em>26</em></div>
        <p>Lorem ipsum is a dummy text only.<br>Dolor sit amet, consectetur adipiscing<br>elit. Nullam felis mauris....<a>[Read more]</a></p>
      </div>
    </div>
    <div class="abs panel video">
      <div class="side-title">Featured Video</div>
      <div class="player" role="img" aria-label="Video still of a house with red roof and garden at dusk">
        <svg width="204" height="120" viewBox="0 0 204 120">
          <circle cx="101" cy="53" r="27" fill="none" stroke="#fff" stroke-width="3"/>
          <path d="M94 40 L113 53 L94 66 Z" fill="#fff"/>
          <rect x="0" y="104" width="204" height="16" fill="rgba(0,0,0,.6)"/>
          <rect x="18" y="111" width="120" height="2" fill="#888"/>
          <rect x="18" y="111" width="40" height="2" fill="#d33"/>
        </svg>
      </div>
    </div>
  </aside>
</main>

<footer>
  <div class="abs footer"></div>
  <div class="abs foot-brand">J.Harlow &amp; Associates</div>
  <div class="abs contact">
    <h4>J. Harlow &amp; Associates, Inc.</h4>
    <p>1245 Lorem Road, Dummy State 2465</p>
    <p><svg width="17" height="12" viewBox="0 0 17 12"><rect x="0.5" y="0.5" width="16" height="11" fill="none" stroke="#fff"/><path d="M1 1 L8.5 7 L16 1" fill="none" stroke="#fff"/></svg>Email: jharlow@info.com</p>
    <p><svg width="17" height="17" viewBox="0 0 17 17"><circle cx="8.5" cy="8.5" r="7.5" fill="none" stroke="#fff"/><path d="M6 4.5 L7.5 6.5 L6.8 7.6 Q7.8 9.6 9.6 10.3 L10.6 9.6 L12.5 11 L11.5 12.5 Q7 12 4.6 6.2 Z" fill="#fff"/></svg>Phone: (555) 145-56879</p>
  </div>
  <div class="abs badges"><i></i><i></i><i></i><i></i><i></i><i></i></div>
  <div class="abs bottom">
    <nav><span>Home</span><span>Auctions</span><span>For Sale</span><span>Buyer and Sellers</span><span>Brokerage</span><span>About Us</span><span>Contact Us</span></nav>
    <div class="copy">Copyright©J.Harlow 2014. All Rights Reserved</div>
  </div>
</footer>
</body>
</html>
```